High-End audio shop owner needs a business card

I need a personal Business Card for my Audio shop which exists since 1962. We offer high Quality brands, professional Attention and run our own repair-service-department. I look for a design which will be printed on high Quality paper and shall convey trust to the Client that we are very serious. Language is german.

```html
<!DOCTYPE html>
<html lang="de">
<head>
<meta charset="utf-8">
<title>Klangwerk Adler – Visitenkarte</title>
<link href="https://fonts.googleapis.com/css2?family=Lato:wght@400;900&display=swap" rel="stylesheet">
<style>
  :root {
    --backdrop: #2b2b2b;
    --card-dark: #161616;
    --card-light: #ffffff;
    --accent: #f07a28;
    --text-grey: #6b6b6b;
    --text-dark-grey: #5a5a5a;
  }
  * { box-sizing: border-box; margin: 0; padding: 0; }
  html, body {
    width: 1200px; height: 900px; overflow: hidden;
    background: var(--backdrop);
    font-family: "Lato", sans-serif;
  }
  .sheet {
    position: relative; width: 1200px; height: 900px;
    display: flex; flex-direction: column; align-items: center; justify-content: center; gap: 44px;
  }
  .card {
    width: 630px; height: 360px; position: relative;
    box-shadow: 0 10px 28px rgba(0,0,0,.45);
  }
  .card--front {
    background: var(--card-dark);
    display: flex; align-items: center; justify-content: center;
  }
  .brand-name {
    font-weight: 900; color: var(--accent);
    letter-spacing: 1px; white-space: nowrap;
  }
  .card--front .brand-name { font-size: 44px; }
  .card--back { background: var(--card-light); }
  .card--back .brand-name {
    position: absolute; left: 48px; top: 160px; font-size: 24px;
  }
  .contact {
    position: absolute; left: 365px; top: 44px; color: var(--text-grey);
  }
  .contact__name {
    font-size: 30px; font-weight: 400; color: var(--text-dark-grey); line-height: 1;
  }
  .contact__role {
    font-size: 15px; color: var(--accent); margin-top: 4px; letter-spacing: .5px;
  }
  .contact__list { list-style: none; margin-top: 22px; }
  .contact__item {
    display: flex; align-items: center; gap: 10px;
    font-size: 18px; line-height: 1; margin-bottom: 12px;
  }
  .contact__icon { width: 14px; height: 14px; flex: none; fill: var(--accent); }
  .contact__address { margin-top: 20px; font-size: 18px; line-height: 1.4; }
</style>
</head>
<body>
<main class="sheet">
  <section class="card card--front">
    <span class="brand-name">KLANGWERK ADLER</span>
  </section>

  <section class="card card--back">
    <span class="brand-name">KLANGWERK ADLER</span>
    <div class="contact">
      <h1 class="contact__name">YOUR NAME</h1>
      <p class="contact__role">OWNER</p>
      <ul class="contact__list">
        <li class="contact__item">
          <svg class="contact__icon" viewBox="0 0 24 24"><path d="M6.6 10.8a15.5 15.5 0 0 0 6.6 6.6l2.2-2.2a1 1 0 0 1 1-.25 11.4 11.4 0 0 0 3.6.57 1 1 0 0 1 1 1V20a1 1 0 0 1-1 1A17 17 0 0 1 3 4a1 1 0 0 1 1-1h3.5a1 1 0 0 1 1 1c0 1.25.2 2.45.57 3.57a1 1 0 0 1-.25 1z"/></svg>
          000 000 0000
        </li>
        <li class="contact__item">
          <svg class="contact__icon" viewBox="0 0 24 24"><path d="M2 5h20v14H2z M3.5 6.5 12 13l8.5-6.5" fill="var(--accent)" stroke="#fff" stroke-width="1.5"/></svg>
          youremail@xyz.com
        </li>
        <li class="contact__item">
          <svg class="contact__icon" viewBox="0 0 24 24"><circle cx="12" cy="12" r="10" fill="none" stroke="var(--accent)" stroke-width="2"/><path d="M2 12h20M12 2c3 3 3 17 0 20M12 2c-3 3-3 17 0 20" fill="none" stroke="var(--accent)" stroke-width="1.6"/></svg>
          www.yourwebsite.com
        </li>
      </ul>
      <p class="contact__address">0000, Street Name<br>City, State 0000</p>
    </div>
  </section>
</main>
</body>
</html>
```